Finding Amber Gate Keepers (Book cover)

This project is for a book I am currently writing. It will help pastors and church leaders communicate why serving in the local church is the so important and how to motivate them to serve at high levels.

The title of the book comes from the passage of scripture where Jesus said, "when a solider demands you to carry his gear one mile, go with him two." He wants his followers to willingly do more than is expected. Doing the minimum seldom does much to change hearts of people around us.

This book will deal with these concepts and help leaders train others to follow in this line of thinking - to be Amber Gate Keepers.

Target Market(s)

church leaders, christian book readers

Industry/Entity Type

Church

Font styles to use
Sans Serif

Colors
fece3e

Requirements
Must have
• Catchy color, font layout to attract readers to take a 2nd look inside the book. Lots of empty space on the cover art, gradient color, sharp contrasts. Large Letters
Nice to have
• A central image on the artwork that will communicate the metaphor of going the 2nd mile.
Should not have
• any imagery that is suggestive

```html
<!DOCTYPE html>
<html lang="en">
<head>
<meta charset="utf-8">
<title>Finding Amber Gate Keepers — Book Cover</title>
<link href="https://fonts.googleapis.com/css2?family=Exo+2:wght@300;700&family=Crimson+Text:ital@1&family=Cinzel:wght@400&display=swap" rel="stylesheet">
<style>
  :root {
    --paper: #ffffff;
    --rule-red: #b8403a;
    --ink: #1e1e1e;
    --title-light: #3a3d42;
    --title-dark: #2b2e33;
    --title-mid: #55595f;
    --sea: #7fa3b8;
    --amber: #fece3e;
    --amber-deep: #e7b823;
  }
  * { margin: 0; padding: 0; box-sizing: border-box; }
  html, body {
    width: 763px;
    height: 1200px;
    overflow: hidden;
    background: var(--paper);
  }
  .cover {
    position: relative;
    width: 763px;
    height: 1200px;
    background: var(--paper);
  }
  .top-rule {
    position: absolute;
    left: 72px;
    top: 35px;
    width: 630px;
    height: 3px;
    background: var(--rule-red);
  }
  .epigraph {
    position: absolute;
    left: 0;
    top: 50px;
    width: 763px;
    text-align: center;
    font-family: "Crimson Text", Georgia, serif;
    font-style: italic;
    font-size: 16px;
    line-height: 19px;
    color: var(--ink);
  }
  .epigraph .ref { display: block; padding-left: 140px; }
  .title {
    position: absolute;
    left: 0;
    top: 120px;
    width: 763px;
    height: 340px;
  }
  .title .kicker {
    font-family: "Exo 2", sans-serif;
    font-weight: 300;
    fill: var(--title-light);
  }
  .title .headline {
    font-family: "Exo 2", sans-serif;
    font-weight: 700;
    fill: url(#titleInk);
  }
  .scene {
    position: absolute;
    left: 0;
    top: 500px;
    width: 763px;
    height: 650px;
    background: linear-gradient(
      to bottom,
      rgba(255,255,255,0) 0%,
      rgba(231,184,35,0.18) 45%,
      var(--sea) 62%,
      var(--amber) 66%,
      var(--amber-deep) 88%,
      rgba(254,206,62,0) 100%
    );
  }
  .author {
    position: absolute;
    left: 0;
    top: 1132px;
    width: 763px;
    text-align: center;
    font-family: "Cinzel", "Times New Roman", serif;
    font-size: 40px;
    letter-spacing: 1px;
    color: var(--ink);
  }
</style>
</head>
<body>
<main class="cover">
  <div class="top-rule"></div>
  <p class="epigraph">"When a soldier demands you to carry his gear one mile, go with him two."<span class="ref">Matthew 5:41</span></p>

  <svg class="title" viewBox="0 120 763 340" width="763" height="340" aria-label="Finding Amber Gate Keepers">
    <defs>
      <linearGradient id="titleInk" x1="0" y1="0" x2="1" y2="1">
        <stop offset="0" stop-color="#55595f"/>
        <stop offset="0.5" stop-color="#2b2e33"/>
        <stop offset="1" stop-color="#45494f"/>
      </linearGradient>
    </defs>
    <text class="kicker" x="68" y="176" font-size="62" textLength="628" lengthAdjust="spacing">FINDING</text>
    <text class="headline" x="66" y="306" font-size="118" textLength="630" lengthAdjust="spacingAndGlyphs">AMBER GATE</text>
    <text class="headline" x="66" y="446" font-size="148" textLength="630" lengthAdjust="spacingAndGlyphs">KEEPERS</text>
  </svg>

  <div class="scene" role="img" aria-label="Painted illustration: a young man walks away along an amber shore by the sea while an older man carries a cardboard box on his shoulder beside a mile marker post"></div>

  <p class="author">DALE WHITMORE</p>
</main>
</body>
</html>
```